Lanterns on the Tide

I need a book cover design for a world history book written for a target audience of high school students and progressive teachers. The book is more balanced towards a world history perspective than a Western-leaning perspective. The first 500 pages deal with the major turning points in world history - from the first hominids that roamed Africa to the end of the Cold War, and the final 100 pages cover the major challenges facing the world today. The book is 95% graphic details, hopefully-engaging stories and needed facts, but there is a bit of sarcasm, verbal irony and asides thrown in to keep the reader's eyes from glossing over. I would need a cover that would appeal to any school teacher, but something that would not scare off students or the average Joe off the street.
Updates

One added note, please leave the bottom right corner -  2" height by 3" width free of text/image for the ISBN code.

As far as a central image goes, it needs to be a dynamic (avoid something readers would readily see elsewhere in their lives) image, or nothing at all.  Also, please justify all text on the back cover to the left side (avoid centering).

Reason: A few people have voiced an interest in having the deadline extended through next weekend to allow for some alterations and also the ability to take advantage of the upcoming holidays. I will take you up on this request. Thank you all again for your submissions. i've seen some very unique takes on the story/tone of the book.

Industry/Entity Type

High School

Requirements
Must have
• I've enclosed a PDF with the text for the front and back cover.

On the back cover, I'd like the quote and the initial question to stand out. I'd like the initial question to be in lower case.

For the spine, I'd like the title font to match the title front from the front cover.

The book cover needs to measure 9.25" by 13.75" with a 1.5" spine. Allow .125 inches for the bleed.

I've attached a Word Document with all the text. The layout is just a suggestion.
Should not have
• I do not want any stock images that I'll need to pay for.

```html
<!DOCTYPE html>
<html lang="en">
<head>
<meta charset="utf-8">
<title>Lanterns on the Tide — Book Cover</title>
<link rel="stylesheet" href="https://fonts.googleapis.com/css2?family=Anton&family=Roboto+Condensed:wght@700&display=swap">
<style>
  :root {
    --page-bg: #f1f1f1;
    --cover-bg: #ffffff;
    --ink: #111111;
    --accent-red: #e0242b;
    --edge: #dcdcdc;
  }
  html, body {
    margin: 0;
    padding: 0;
    width: 1200px;
    height: 900px;
    overflow: hidden;
    background: var(--page-bg);
  }
  .stage {
    position: relative;
    width: 1200px;
    height: 900px;
  }
  .cover {
    position: absolute;
    left: 338px;
    top: 60px;
    width: 524px;
    height: 780px;
    background: var(--cover-bg);
    border: 1px solid var(--edge);
    box-sizing: border-box;
    overflow: hidden;
  }
  .globe-art {
    position: absolute;
    left: 40px;
    top: 110px;
    width: 444px;
    height: 400px;
  }
  .title {
    position: absolute;
    left: 0;
    right: 0;
    top: 70px;
    margin: 0;
    text-align: center;
    font-family: "Anton", "Impact", sans-serif;
    font-weight: 400;
    font-size: 104px;
    line-height: 1.18;
    letter-spacing: 0.5px;
    color: var(--ink);
    text-transform: uppercase;
  }
  .title span { display: block; }
  .subtitle {
    position: absolute;
    left: 0;
    right: 0;
    top: 566px;
    margin: 0 auto;
    width: 300px;
    text-align: center;
    font-family: "Roboto Condensed", "Arial Narrow", sans-serif;
    font-weight: 700;
    font-size: 15px;
    line-height: 1.25;
    color: var(--ink);
  }
  .author {
    position: absolute;
    left: 0;
    right: 0;
    bottom: 82px;
    margin: 0;
    text-align: center;
    font-family: "Roboto Condensed", "Arial Narrow", sans-serif;
    font-weight: 700;
    font-size: 24px;
    letter-spacing: 0.5px;
    color: var(--ink);
    text-transform: uppercase;
  }
</style>
</head>
<body>
  <main class="stage">
    <section class="cover">
      <svg class="globe-art" viewBox="0 0 444 400" role="img" aria-label="Globe formed from scattered red map fragments of the world's countries">
        <ellipse cx="222" cy="200" rx="206" ry="192" fill="var(--accent-red)"/>
      </svg>
      <h1 class="title">
        <span>Lanterns</span>
        <span>on the</span>
        <span>Tide</span>
      </h1>
      <p class="subtitle">The tales, traditions and turning points of world history and the regional changes of today</p>
      <p class="author">Paul Hendry</p>
    </section>
  </main>
</body>
</html>
```